Gelato Business Card

create a new business card using existing logo

Target Market(s)

B2B

Contact Information for Business Card

typical contact info: logo, address, email, phone, rep name

Colors
0355a3
33a6d7

Requirements
Must have
• a feel of high quality, luxury, happiness
• use cool, comforting color and texture of business card.
Nice to have
• "A Little Perfection Goes A Long Way!" TM
• or, "more quality, more flavor"
• or, "Flavor Matters"

```html
<!DOCTYPE html>
<html lang="en">
<head>
<meta charset="utf-8">
<title>Bellavista Artisan Gelato – Business Card</title>
<link href="https://fonts.googleapis.com/css2?family=Lato:wght@400;700&display=swap" rel="stylesheet">
<style>
  :root {
    --backdrop: #202020;
    --card: #1c1c1c;
    --card-edge: #2a2a2a;
    --silver: #cfcfcf;
    --brand-blue: #4043a8;
    --accent-blue: #33a6d7;
    --ink-light: #f2f2f2;
  }
  * { margin: 0; padding: 0; box-sizing: border-box; }
  html, body {
    width: 1200px; height: 900px; overflow: hidden;
    background: var(--backdrop);
    font-family: 'Lato', Arial, sans-serif;
  }
  .stage { position: relative; width: 1200px; height: 900px; }
  .card {
    position: absolute; left: 280px;
    width: 640px; height: 366px;
    background: var(--card);
    border: 1px solid var(--card-edge);
    box-shadow: 0 14px 30px rgba(0,0,0,.55);
  }
  .card--front { top: 50px; display: flex; align-items: center; justify-content: center; }
  .card--back { top: 470px; }

  .brand { display: flex; align-items: center; gap: 12px; }
  .brand__dot { width: 22px; height: 22px; border-radius: 50%; background: currentColor; flex: none; }
  .brand__name { font-weight: 700; font-size: 34px; letter-spacing: 1px; white-space: nowrap; }
  .brand--front { color: var(--silver); }
  .brand--back {
    color: var(--brand-blue);
    position: absolute; left: 0; top: 0;
    width: 330px; height: 366px;
    justify-content: center;
    padding: 0 24px;
  }
  .brand--back .brand__name { font-size: 21px; letter-spacing: .5px; }
  .brand--back .brand__dot { width: 16px; height: 16px; }

  .divider {
    position: absolute; left: 330px; top: 70px;
    width: 2px; height: 226px; background: var(--brand-blue);
  }
  .contact { position: absolute; left: 356px; top: 70px; color: var(--ink-light); }
  .contact__name {
    font-weight: 700; font-size: 27px; letter-spacing: 2px;
    color: var(--brand-blue); text-transform: uppercase;
  }
  .contact__role { font-size: 18px; margin-bottom: 18px; }
  .contact__address { font-size: 16px; line-height: 1.35; margin-bottom: 14px; }
  .contact__list { list-style: none; font-size: 16px; line-height: 1.45; }
  .contact__list li { display: flex; align-items: center; gap: 10px; }
  .contact__list svg { width: 14px; height: 14px; flex: none; }
</style>
</head>
<body>
<main class="stage">
  <section class="card card--front">
    <div class="brand brand--front">
      <span class="brand__dot"></span>
      <span class="brand__name">BELLAVISTA ARTISAN GELATO</span>
    </div>
  </section>

  <section class="card card--back">
    <div class="brand brand--back">
      <span class="brand__dot"></span>
      <span class="brand__name">BELLAVISTA GELATO</span>
    </div>
    <div class="divider"></div>
    <div class="contact">
      <p class="contact__name">Daniel Moreno</p>
      <p class="contact__role">Director</p>
      <p class="contact__address">2450 Harbor Way, Suite 12<br>Larkspur, CA 94939 United States</p>
      <ul class="contact__list">
        <li><svg viewBox="0 0 16 16"><path d="M4 1l3 3-2 2c1 2 3 4 5 5l2-2 3 3-2 3C7 15 1 9 1 3z" fill="#4043a8"/></svg>(415) 555-0142</li>
        <li><svg viewBox="0 0 16 16"><rect x="4" y="1" width="8" height="4" fill="#4043a8"/><rect x="1" y="6" width="14" height="6" rx="1" fill="#4043a8"/><rect x="4" y="10" width="8" height="5" fill="#4043a8"/></svg>(415) 555-0187</li>
        <li><svg viewBox="0 0 16 16"><rect x="1" y="3" width="14" height="10" fill="none" stroke="#4043a8" stroke-width="1.5"/><path d="M1 3l7 6 7-6" fill="none" stroke="#4043a8" stroke-width="1.5"/></svg>hello@bellavistagelato.com</li>
        <li><svg viewBox="0 0 16 16"><circle cx="8" cy="8" r="6.5" fill="none" stroke="#4043a8" stroke-width="1.3"/><ellipse cx="8" cy="8" rx="3" ry="6.5" fill="none" stroke="#4043a8" stroke-width="1.1"/><path d="M1.5 8h13" stroke="#4043a8" stroke-width="1.1"/></svg>www.bellavistagelato.com</li>
      </ul>
    </div>
  </section>
</main>
</body>
</html>
```